political campaign lawn sign - Governor's Council in Massachuesetts

We are looking for a political lawn sign. We are running a campaign for Governor's Council in Massachusetts. This sign will be on the lawn of homes and businesses so people driving by will see it. It needs to be simple and bold. The last name is long so maybe it could say vote for Marty and then Kolbeck will be big a bold on the next line??
We need it to say:
Vote for Martin Kolbeck
Governor's Council.

Target Market(s)

local residents

Industry/Entity Type

Politcal Campaign

Font styles to use
Sans Serif
Other font styles liked:
• not sure what font but a modern looking one such as Helvetica, Arial, Sans Seri, sharp sans..

Colors
0054AA
0677BA
7BADD7
CADEEF
E8F1F8
00AB8E
00BBA5
67D7C9
C6EFE9
E9F9F6
FFF300
FFF600
FEFA6F
FFFEC7
FFFEE8

Requirements
Must have
• My name written out with a Capital D and R but lower case for every other letter so its Marty Kolbeck
Nice to have
• modern font , the Colors of the lawn sign should have Blue, Yellow and White something bold that will stand out
Should not have
• any maps of Massachusetts

```html
<!DOCTYPE html>
<html lang="en">
<head>
<meta charset="utf-8">
<title>Martin Kolbeck – Governor's Council Lawn Sign</title>
<link rel="stylesheet" href="https://fonts.googleapis.com/css2?family=Archivo:wght@800&family=Oswald:wght@700&display=swap">
<style>
  :root {
    --navy: #1f2d5e;
    --gold: #e8ad2c;
    --white: #ffffff;
    --backdrop: #ececec;
  }
  html, body {
    margin: 0;
    padding: 0;
    width: 1200px;
    height: 1118px;
    overflow: hidden;
    background: var(--backdrop);
  }
  .lawn-sign {
    position: absolute;
    left: 40px;
    top: 139px;
    width: 1120px;
    height: 840px;
    display: block;
  }
  .sign-field { fill: var(--navy); }
  .sign-footer { fill: var(--white); }
  .accent-block { fill: var(--gold); }
  .vote-for {
    font-family: "Archivo", "Helvetica Neue", Arial, sans-serif;
    font-weight: 800;
    fill: var(--white);
  }
  .candidate-name {
    font-family: "Archivo", "Helvetica Neue", Arial, sans-serif;
    font-weight: 800;
    fill: var(--gold);
  }
  .office-title {
    font-family: "Oswald", "Arial Narrow", sans-serif;
    font-weight: 700;
    fill: var(--navy);
  }
</style>
</head>
<body>
<svg class="lawn-sign" viewBox="0 0 1240 930" xmlns="http://www.w3.org/2000/svg" role="img" aria-label="Vote for Martin Kolbeck, Governor's Council">
  <rect class="sign-field" x="0" y="0" width="1240" height="682"/>
  <rect class="sign-footer" x="0" y="682" width="1240" height="248"/>

  <rect class="accent-block" x="68" y="0" width="390" height="370"/>
  <rect class="accent-block" x="506" y="0" width="654" height="42"/>

  <text class="vote-for" x="105" y="187" font-size="190" textLength="318" lengthAdjust="spacingAndGlyphs">Vote</text>
  <text class="vote-for" x="165" y="342" font-size="190" textLength="198" lengthAdjust="spacingAndGlyphs">for</text>

  <text class="candidate-name" x="505" y="352" font-size="326" textLength="655" lengthAdjust="spacingAndGlyphs">Martin</text>
  <text class="candidate-name" x="72" y="632" font-size="305" textLength="1090" lengthAdjust="spacingAndGlyphs">Kolbeck</text>

  <text class="office-title" x="72" y="867" font-size="182" textLength="1088" lengthAdjust="spacingAndGlyphs">Governor's Council</text>
</svg>
</body>
</html>
```